Market Research firm needs updated business cards with new logo

We need the logo to be included somewhere on the card (attached). We would also like the phrases "Independent, Objective, Comprehensive" and "Research You Can Trust" somewhere on the card. Front or back. Our colors are hex codes 6075a7, e48d25 and 5a5b5b. Though you are certainly not limited to those shades, whatever you produce should coordinate with them. I have also attached our favicon. Feel free to use it in your design, but please do not use it to replace the full logo.

Contact Information for Business Card

see project description

Font styles to use
Other font styles liked:
• Open Sans

Requirements
Must have
• the logo
• We use Open Sans font

```html
<!DOCTYPE html>
<html lang="en">
<head>
<meta charset="utf-8">
<title>Veldra Insights — Business Card</title>
<link rel="stylesheet" href="https://fonts.googleapis.com/css2?family=Open+Sans:wght@400;600&display=swap">
<style>
  :root {
    --stage: #2a2a2a;
    --slate: #6b7a89;
    --slate-dark: #5e6c7b;
    --orange: #f0801f;
    --ink: #5a5b5b;
    --paper: #ffffff;
    --rule: #6b7a89;
  }
  * { box-sizing: border-box; margin: 0; padding: 0; }
  html, body {
    width: 1200px; height: 895px; overflow: hidden;
    background: var(--stage);
    font-family: "Open Sans", sans-serif;
  }
  .stage {
    width: 1200px; height: 895px;
    display: flex; flex-direction: column; align-items: center; justify-content: center;
    gap: 48px;
  }
  .card {
    position: relative;
    width: 640px; height: 366px;
    border-radius: 22px;
    overflow: hidden;
    box-shadow: 0 10px 30px rgba(0,0,0,.45);
  }

  /* Back side */
  .card-back { background: var(--slate); }
  .card-back .brand {
    position: absolute; left: 0; right: 0; top: 130px;
    text-align: center;
    font-size: 54px; font-weight: 400; letter-spacing: -0.5px;
    color: var(--paper);
  }
  .card-back .values {
    position: absolute; left: 0; right: 0; top: 222px;
    text-align: center;
    font-size: 14px; letter-spacing: 2px;
    color: var(--paper);
  }

  /* Front side */
  .card-front { background: var(--paper); color: var(--ink); }
  .front-brand {
    position: absolute; left: 250px; top: 44px;
    font-size: 40px; font-weight: 400; letter-spacing: -0.5px;
    color: var(--slate);
  }
  .front-phone {
    position: absolute; left: 254px; top: 100px;
    font-size: 14px; letter-spacing: 1px; color: var(--ink);
  }
  .divider {
    position: absolute; left: 230px; right: 36px; top: 196px;
    height: 1px; background: var(--rule);
  }
  .person { position: absolute; left: 40px; top: 172px; }
  .person-name { font-size: 30px; font-weight: 600; color: var(--orange); line-height: 1.1; }
  .person-title { font-size: 16px; color: var(--ink); margin-top: 2px; }
  .contacts { list-style: none; margin-top: 12px; }
  .contacts li {
    display: flex; align-items: center; gap: 10px;
    font-size: 15px; line-height: 22px; color: var(--ink);
  }
  .contacts svg { width: 13px; height: 13px; flex: none; fill: var(--orange); }
  .address {
    position: absolute; right: 40px; top: 222px;
    text-align: right; font-size: 15px; line-height: 22px; color: var(--ink);
  }
  .footer-shapes { position: absolute; left: 0; bottom: 0; width: 640px; height: 60px; }
  .trust-line {
    position: absolute; right: 34px; bottom: 22px;
    font-size: 15px; letter-spacing: .5px; color: var(--paper);
  }
</style>
</head>
<body>
<main class="stage">

  <section class="card card-back" aria-label="Card back">
    <div class="brand">Veldra Insights</div>
    <p class="values">Independent, Objective, Comprehensive</p>
  </section>

  <section class="card card-front" aria-label="Card front">
    <div class="front-brand">Veldra Insights</div>
    <div class="front-phone">000 000 0000</div>
    <div class="divider"></div>

    <div class="person">
      <div class="person-name">Daniel Hart</div>
      <div class="person-title">Founder &amp; CEO</div>
      <ul class="contacts">
        <li>
          <svg viewBox="0 0 16 16" aria-hidden="true"><path d="M3 1l3 3-2 2c1 2 3 4 5 5l2-2 3 3-2 3C6 15 1 10 0 4z"/></svg>
          000 000 0000
        </li>
        <li>
          <svg viewBox="0 0 16 16" aria-hidden="true"><path d="M4 0h8a1 1 0 0 1 1 1v14a1 1 0 0 1-1 1H4a1 1 0 0 1-1-1V1a1 1 0 0 1 1-1zm1 2v10h6V2zm3 11a1 1 0 1 0 0 2 1 1 0 0 0 0-2z"/></svg>
          000 000 0000
        </li>
        <li>
          <svg viewBox="0 0 16 16" aria-hidden="true"><path d="M0 3h16v1L8 9 0 4zm0 3l8 5 8-5v7H0z"/></svg>
          info@veldrainsights.com
        </li>
        <li>
          <svg viewBox="0 0 16 16" aria-hidden="true"><path d="M8 0a8 8 0 1 0 0 16A8 8 0 0 0 8 0zm-1 2v3H4.5A6 6 0 0 1 7 2zm2 0a6 6 0 0 1 2.5 3H9zM2.3 7H7v2H2.3a6 6 0 0 1 0-2zM9 7h4.7a6 6 0 0 1 0 2H9zm-4.5 4H7v3a6 6 0 0 1-2.5-3zM9 11h2.5A6 6 0 0 1 9 14z"/></svg>
          www.veldrainsights.com
        </li>
      </ul>
    </div>

    <address class="address" style="font-style:normal">
      4820 Alder Ave, Suite B<br>
      Maple Grove, CA 90415
    </address>

    <svg class="footer-shapes" viewBox="0 0 640 60" aria-hidden="true">
      <polygon points="0,48 400,48 410,20 640,20 640,60 0,60" fill="var(--slate)"/>
      <polygon points="410,12 640,12 640,52 400,52" fill="var(--orange)"/>
    </svg>
    <div class="trust-line">Research You Can Trust</div>
  </section>

</main>
</body>
</html>
```